DEAN COLLOPY PROPERTY SERVICES

I want a business card that is clean and simple.
'Dean Collopy Property Services' is the title.
Somewhere on the card needs to be 'Carpentry, Tiling, painting and garden services'

On the back of card
PH 087 394 1526
email: deancollopypropertyservices@fernmail.net

I have attached a picture of my other business. I would like the font and design to be similar to the bathroom business.

Many thanks.

```html
<!DOCTYPE html>
<html lang="en">
<head>
<meta charset="utf-8">
<title>Dean Collopy Property Services – Business Card</title>
<link rel="stylesheet" href="https://fonts.googleapis.com/css2?family=Lato:wght@300;400;700;900&display=swap">
<style>
  :root {
    --backdrop: #d6d6d6;
    --card-dark: #0b0b0b;
    --card-light: #f7f7f7;
    --ink: #111111;
    --ink-on-dark: #ffffff;
    --shadow: rgba(0, 0, 0, 0.22);
  }
  * { box-sizing: border-box; margin: 0; padding: 0; }
  html, body {
    width: 1200px;
    height: 800px;
    overflow: hidden;
    background: var(--backdrop);
    font-family: "Lato", sans-serif;
  }
  .stage {
    width: 1200px;
    height: 800px;
    display: flex;
    align-items: center;
    justify-content: center;
    gap: 60px;
  }
  .card {
    position: relative;
    width: 520px;
    height: 306px;
    border-radius: 4px;
    box-shadow: 0 14px 30px var(--shadow);
    overflow: hidden;
  }

  /* Dark side */
  .card--services {
    background: var(--card-dark);
    color: var(--ink-on-dark);
  }
  .services__rule {
    position: absolute;
    left: 50%;
    top: 0;
    width: 4px;
    height: 110px;
    margin-left: -2px;
    background: var(--ink-on-dark);
  }
  .services__list {
    position: absolute;
    left: 0;
    right: 0;
    top: 170px;
    text-align: center;
    font-weight: 300;
    font-size: 17px;
    letter-spacing: 0.06em;
    line-height: 1.5;
    text-transform: uppercase;
  }

  /* Light side */
  .card--contact {
    background: var(--card-light);
    color: var(--ink);
  }
  .contact__band {
    position: absolute;
    left: 28px;
    top: 52px;
    bottom: 0;
    width: 14px;
    background: var(--ink);
  }
  .sister-brand {
    position: absolute;
    right: 36px;
    top: 42px;
    font-weight: 400;
    font-size: 30px;
    letter-spacing: 0.01em;
    color: var(--ink);
  }
  .contact__details {
    position: absolute;
    left: 66px;
    bottom: 34px;
  }
  .contact__name {
    font-weight: 900;
    font-size: 25px;
    line-height: 1.1;
    margin-bottom: 12px;
    width: 300px;
  }
  .contact__line {
    display: flex;
    align-items: center;
    gap: 8px;
    font-weight: 400;
    font-size: 16px;
    line-height: 1.5;
  }
  .contact__icon {
    width: 16px;
    height: 16px;
    flex: none;
  }
</style>
</head>
<body>
  <main class="stage">
    <section class="card card--services" aria-label="Card front">
      <div class="services__rule"></div>
      <p class="services__list">Carpentry, Tiling, Painting<br>and Garden Services</p>
    </section>

    <section class="card card--contact" aria-label="Card back">
      <div class="contact__band"></div>
      <p class="sister-brand">Collopy Bathrooms</p>
      <div class="contact__details">
        <h1 class="contact__name">Dean Collopy Property Services</h1>
        <p class="contact__line">
          <svg class="contact__icon" viewBox="0 0 16 16" aria-hidden="true">
            <rect x="1" y="1" width="14" height="14" rx="4" fill="none" stroke="currentColor" stroke-width="1.3"/>
            <path d="M5.5 4.2c.5 0 .9.9 1 1.4.1.4-.6.8-.6 1.2.3.9 1.1 1.8 2 2.2.4 0 .8-.7 1.2-.6.5.1 1.4.5 1.4 1 0 .9-.8 1.5-1.6 1.4C6.6 10.5 4.6 8.5 4.3 6c-.1-.9.4-1.8 1.2-1.8z" fill="currentColor"/>
          </svg>
          087 394 1526
        </p>
        <p class="contact__line">
          <svg class="contact__icon" viewBox="0 0 16 16" aria-hidden="true">
            <circle cx="8" cy="8" r="7.5" fill="currentColor"/>
            <rect x="3.8" y="5" width="8.4" height="6" rx="0.6" fill="none" stroke="#f7f7f7" stroke-width="1"/>
            <path d="M4 5.4 8 8.4l4-3" fill="none" stroke="#f7f7f7" stroke-width="1"/>
          </svg>
          deancollopypropertyservices@fernmail.net
        </p>
      </div>
    </section>
  </main>
</body>
</html>
```